Recipe mobile app, new flow and design for uploading recipe process

I need a new recipe upload process that's simple, intuitive, and engaging.
The goal is to have a user-friendly and fast flow.
The app is a social recipe library where anyone can upload a recipe after signing up. I currently have a flow, but it's "boring," so I'd like to significantly improve this aspect of the app.
When I create a new recipe, it's immediately saved and labeled as a draft. I'll then need to specify:
- Recipe title
- Cover image (required)
- Number of people (how many people is the recipe for)
- Ingredients (name, quantity, and unit of measurement)
- Recipe explanation (broken down into steps, and I can optionally attach an image to each step)
- Upload
Every change is immediately saved, so you can edit, exit, and resume editing later.
I've attached images of the app and the current upload process.
Thank you.
Low design quality
Good morning everyone,
some of the designs received are fantastic, but please make sure to carefully read the requirement so as not to do extra work.
The requirement is to redesign the flow that a user follows when uploading a recipe to the platform.
We have uploaded the current app screens to give you an idea of what the product looks like, what the colors and style are, but we don’t need a full redesign - only the part mentioned above, while keeping the existing style and colors (we cannot rework the entire theme).
To clarify: if you look at the screens shared in the zip file attached to the project, the focus should be on the screens from 5_.png to 10_.png.
These screens can be redesigned in the most creative way you think, as long as the overall theme remains unchanged.
Thank you for your attention.

```html
<!DOCTYPE html>
<html lang="en">
<head>
<meta charset="utf-8">
<title>Recipe Mobile App – Upload Flow</title>
<link href="https://fonts.googleapis.com/css2?family=Inter:wght@400;500;600;700;800&display=swap" rel="stylesheet">
<style>
:root{
  --ink:#0c1d1a;
  --muted:#5d6b67;
  --green:#3db08f;
  --green-text:#1e8a6b;
  --line:#dfe5e2;
  --white:#ffffff;
  --red:#ee1d24;
  --bg-top:#58cba7;
  --bg-mid:#c6f7e4;
  --bg-low:#cbf9d6;
  --bg-bottom:#eaf1dc;
}
*{box-sizing:border-box;margin:0;padding:0}
html,body{width:800px;height:1200px;overflow:hidden}
body{font-family:"Inter",sans-serif;color:var(--ink);background:var(--bg-mid)}
.board{
  position:absolute;left:0;top:0;width:1568px;height:2352px;
  transform:scale(0.5102);transform-origin:0 0;
  background:
    radial-gradient(ellipse 700px 500px at 1500px 100px, rgba(180,240,220,.55), transparent 70%),
    radial-gradient(ellipse 600px 500px at 0px 200px, rgba(170,235,215,.6), transparent 70%),
    linear-gradient(180deg,var(--bg-top) 0%,#7fdcbd 18%,var(--bg-mid) 45%,var(--bg-low) 72%,var(--bg-bottom) 100%);
}
.grid{
  position:absolute;left:0;top:0;width:100%;height:420px;
  background-image:
    linear-gradient(rgba(255,255,255,.10) 1px,transparent 1px),
    linear-gradient(90deg,rgba(255,255,255,.10) 1px,transparent 1px);
  background-size:78px 78px;
}
.eyebrow{position:absolute;left:237px;top:94px;font-size:31px;font-weight:600;letter-spacing:1.5px;color:var(--white)}
.headline{position:absolute;left:232px;top:136px;font-size:108px;font-weight:700;letter-spacing:-2px;line-height:1.1;color:#06201b}
.lede{position:absolute;left:237px;top:268px;font-size:26px;font-weight:400;color:#07201b;letter-spacing:-.3px}

.step-label{position:absolute;width:340px;text-align:center}
.step-label .step{font-size:11px;font-weight:500;letter-spacing:.3px;display:block;color:#173a32}
.step-label .name{font-size:18px;font-weight:500;display:block;margin-top:6px}

.phone{
  position:absolute;width:340px;height:734px;border:3px solid #0b0b0b;border-radius:40px;overflow:hidden;
  background:linear-gradient(180deg,#f7fbf6 0%,#ffffff 8%,#eef8e4 40%,#f3fbee 70%,#ffffff 100%);
}
.phone > *{position:absolute}
.back{left:12px;top:50px;width:14px;height:14px}
.progress{left:95px;top:52px;width:144px;height:4px;border-radius:2px;background:#e3ebe7}
.progress i{display:block;height:100%;border-radius:2px;background:var(--green)}
.count{right:12px;top:49px;font-size:12px;font-weight:500}
.screen-title{left:0;right:0;top:86px;text-align:center;font-size:22px;font-weight:700;letter-spacing:-.3px}
.screen-sub{left:0;right:0;top:120px;text-align:center;font-size:11.5px;font-weight:400}
.label{left:27px;font-size:11px;font-weight:500;color:#262f2d}
.field{
  left:24px;width:288px;height:46px;background:var(--white);border:1px solid var(--line);border-radius:8px;
  display:flex;align-items:center;padding-left:14px;font-size:14px;font-weight:500;color:var(--ink)
}
.field.placeholder{color:#8b9693;font-weight:400;font-size:12.5px}
.area{height:71px;align-items:flex-start;padding:9px 10px 0 12px;font-size:11.6px;line-height:1.33;letter-spacing:-.2px}
.area::after{content:"";position:absolute;right:5px;bottom:5px;width:6px;height:6px;border-right:1px solid #aab;border-bottom:1px solid #aab}
.stepper{position:absolute;right:10px;top:9px;display:flex;gap:6px}
.stepper span{width:26px;height:26px;border-radius:50%;background:#eef1f0;display:flex;align-items:center;justify-content:center;font-size:18px;font-weight:400}
.next{
  left:72px;top:659px;width:195px;height:54px;border-radius:27px;background:var(--green);color:var(--white);
  display:flex;align-items:center;justify-content:center;gap:10px;font-size:15px;font-weight:600
}
.upload-box{
  left:27px;top:154px;width:288px;height:225px;border:1.5px dashed #9fbfad;border-radius:8px;background:rgba(255,255,255,.6);
  text-align:center
}
.upload-box .dish{position:absolute;left:74px;top:26px;width:140px;height:86px;border-radius:10px;
  background:linear-gradient(135deg,#f6e3b4 0%,#f1c98a 100%)}
.upload-box .u-title{position:absolute;left:0;right:0;top:122px;font-size:16px;font-weight:600}
.upload-box .u-sub{position:absolute;left:50px;right:50px;top:148px;font-size:10.5px;line-height:1.35;color:#3c4542}
.photo{left:26px;top:157px;width:287px;height:218px;border-radius:6px;
  background:linear-gradient(160deg,#8a8580 0%,#5d524a 45%,#3a3431 100%)}
.edit{left:280px;top:164px;width:27px;height:27px;border-radius:50%;background:var(--white);display:flex;align-items:center;justify-content:center}

.ing-card{left:15px;width:308px;border-radius:12px;background:rgba(255,255,255,.55);box-shadow:0 2px 10px rgba(60,120,90,.08)}
.ing-card > *{position:absolute}
.ing-card .head{left:20px;top:12px;display:flex;align-items:center;gap:8px;font-size:13px;font-weight:500;color:var(--green-text)}
.ing-card .close{right:14px;top:11px;font-size:16px}
.ing-card .label{left:19px}
.ing-card .field{left:16px;width:278px}
.unit{position:absolute;left:170px;top:10px;bottom:10px;border-left:1px solid var(--line);padding-left:10px;display:flex;align-items:center;font-size:12px;font-weight:400;color:#5a6562;width:108px}
.unit svg{position:absolute;right:10px}
.add{left:17px;display:flex;align-items:center;gap:7px;font-size:13px;font-weight:500;color:var(--green-text)}
.add b{width:22px;height:22px;border-radius:50%;background:var(--green);color:var(--white);display:flex;align-items:center;justify-content:center;font-size:18px;font-weight:500}
.flow{position:absolute;left:0;top:0}
</style>
</head>
<body>
<div class="board">
  <div class="grid"></div>
  <p class="eyebrow">FOOD &amp; DRINK</p>
  <h1 class="headline">Recipe Mobile App</h1>
  <p class="lede">New recipe upload process that's simple, intuitive, and engaging.</p>

  <div class="step-label" style="left:222px;top:398px"><span class="step">STEP 1</span><span class="name">Upload Recipe Screen</span></div>
  <div class="step-label" style="left:613px;top:398px"><span class="step">STEP 1</span><span class="name">Upload Recipe Screen</span></div>
  <div class="step-label" style="left:1006px;top:398px"><span class="step">STEP 1</span><span class="name">Upload Recipe Screen</span></div>
  <div class="step-label" style="left:413px;top:1310px"><span class="step">STEP 2</span><span class="name">Upload Recipe Screen</span></div>
  <div class="step-label" style="left:808px;top:1310px"><span class="step">STEP 2</span><span class="name">Upload Recipe Screen</span></div>

  <section class="phone" style="left:222px;top:466px">
    <svg class="back" viewBox="0 0 14 14"><path d="M9 2 4 7l5 5" fill="none" stroke="#111" stroke-width="1.8" stroke-linecap="round"/></svg>
    <div class="progress"><i style="width:32px"></i></div>
    <span class="count">1/4</span>
    <h2 class="screen-title">Upload Recipe Image &amp; Title</h2>
    <p class="screen-sub">Provide recipe image, title and Number of people</p>
    <div class="upload-box">
      <div class="dish" role="img" aria-label="Illustration of a bowl of food"></div>
      <p class="u-title">Upload Recipe Image</p>
      <p class="u-sub">Tap to upload recipe image. Image will be under 10 mb.</p>
    </div>
    <span class="label" style="top:394px">Recipe Title</span>
    <div class="field placeholder" style="top:413px">Type recipe name</div>
    <span class="label" style="top:476px">Number of People</span>
    <div class="field" style="top:495px">1<div class="stepper"><span>−</span><span>+</span></div></div>
    <span class="label" style="top:556px">Description</span>
    <div class="field placeholder area" style="top:574px;font-size:12.5px">Short description about recipe</div>
    <div class="next">Next <svg width="16" height="12" viewBox="0 0 16 12"><path d="M1 6h13M9 1l5 5-5 5" fill="none" stroke="#fff" stroke-width="1.7" stroke-linecap="round" stroke-linejoin="round"/></svg></div>
  </section>

  <section class="phone" style="left:613px;top:466px">
    <svg class="back" viewBox="0 0 14 14"><path d="M9 2 4 7l5 5" fill="none" stroke="#111" stroke-width="1.8" stroke-linecap="round"/></svg>
    <div class="progress"><i style="width:32px"></i></div>
    <span class="count">1/4</span>
    <h2 class="screen-title">Upload Recipe Image &amp; Title</h2>
    <p class="screen-sub">Provide recipe image, title and Number of people</p>
    <div class="photo" role="img" aria-label="Photo of a slice of tiramisu on a plate"></div>
    <div class="edit"><svg width="13" height="13" viewBox="0 0 13 13"><path d="M2 11l.6-2.6L8.8 2.2l2 2-6.2 6.2z" fill="#111"/></svg></div>
    <span class="label" style="top:394px">Recipe Title</span>
    <div class="field" style="top:413px">Tiramisu</div>
    <span class="label" style="top:476px">Number of People</span>
    <div class="field" style="top:495px">4<div class="stepper"><span>−</span><span>+</span></div></div>
    <span class="label" style="top:556px">Description</span>
    <div class="field area" style="top:574px">Tiramisu is a classic Italian no-bake dessert made with layers of coffee-soaked ladyfinger biscuits, creamy mascarpone cheese mixture</div>
    <div class="next">Next <svg width="16" height="12" viewBox="0 0 16 12"><path d="M1 6h13M9 1l5 5-5 5" fill="none" stroke="#fff" stroke-width="1.7" stroke-linecap="round" stroke-linejoin="round"/></svg></div>
  </section>

  <section class="phone" style="left:1006px;top:466px">
    <svg class="back" viewBox="0 0 14 14"><path d="M9 2 4 7l5 5" fill="none" stroke="#111" stroke-width="1.8" stroke-linecap="round"/></svg>
    <div class="progress"><i style="width:60px"></i></div>
    <span class="count">2/4</span>
    <h2 class="screen-title">Ingredients Information</h2>
    <p class="screen-sub">Ingredients name, quantity, and unit of measurement</p>
    <div class="ing-card" style="top:146px;height:202px">
      <div class="head"><svg width="18" height="12" viewBox="0 0 18 12"><path d="M0 0h18l-3 9H3z" fill="#2aa383"/><rect x="4" y="10" width="10" height="2" fill="#2aa383"/></svg>Ingerdients 1</div>
      <span class="label" style="top:34px">Ingredient Name</span>
      <div class="field placeholder" style="top:58px">Type ingredient name</div>
      <span class="label" style="top:119px">Quantity</span>
      <div class="field placeholder" style="top:138px">Type quantity<div class="unit">Unit<svg width="11" height="7" viewBox="0 0 11 7"><path d="M1 1l4.5 4.5L10 1" fill="none" stroke="#333" stroke-width="1.3"/></svg></div></div>
    </div>
    <div class="next">Next <svg width="16" height="12" viewBox="0 0 16 12"><path d="M1 6h13M9 1l5 5-5 5" fill="none" stroke="#fff" stroke-width="1.7" stroke-linecap="round" stroke-linejoin="round"/></svg></div>
  </section>

  <section class="phone" style="left:413px;top:1379px">
    <svg class="back" viewBox="0 0 14 14"><path d="M9 2 4 7l5 5" fill="none" stroke="#111" stroke-width="1.8" stroke-linecap="round"/></svg>
    <div class="progress"><i style="width:52px"></i></div>
    <span class="count">2/4</span>
    <h2 class="screen-title">Ingredients Information</h2>
    <p class="screen-sub">Ingredients name, quantity, and unit of measurement</p>
    <div class="ing-card" style="top:146px;height:202px">
      <div class="head"><svg width="18" height="12" viewBox="0 0 18 12"><path d="M0 0h18l-3 9H3z" fill="#2aa383"/><rect x="4" y="10" width="10" height="2" fill="#2aa383"/></svg>Ingerdients 1</div>
      <span class="label" style="top:34px">Ingredient Name</span>
      <div class="field" style="top:58px">Tiramisu</div>
      <span class="label" style="top:119px">Quantity</span>
      <div class="field" style="top:138px">250<div class="unit">Milliliters<svg width="11" height="7" viewBox="0 0 11 7"><path d="M1 1l4.5 4.5L10 1" fill="none" stroke="#333" stroke-width="1.3"/></svg></div></div>
    </div>
    <div class="add" style="top:363px"><b>+</b>Add Another Ingredient</div>
    <div class="next">Next <svg width="16" height="12" viewBox="0 0 16 12"><path d="M1 6h13M9 1l5 5-5 5" fill="none" stroke="#fff" stroke-width="1.7" stroke-linecap="round" stroke-linejoin="round"/></svg></div>
  </section>

  <section class="phone" style="left:808px;top:1379px">
    <svg class="back" viewBox="0 0 14 14"><path d="M9 2 4 7l5 5" fill="none" stroke="#111" stroke-width="1.8" stroke-linecap="round"/></svg>
    <div class="progress"><i style="width:52px"></i></div>
    <span class="count">2/4</span>
    <h2 class="screen-title">Ingredients Information</h2>
    <p class="screen-sub">Ingredients name, quantity, and unit of measurement</p>
    <div class="ing-card" style="top:146px;height:202px">
      <div class="head"><svg width="18" height="12" viewBox="0 0 18 12"><path d="M0 0h18l-3 9H3z" fill="#2aa383"/><rect x="4" y="10" width="10" height="2" fill="#2aa383"/></svg>Ingerdients 1</div>
      <span class="close">✕</span>
      <span class="label" style="top:34px">Ingredient Name</span>
      <div class="field" style="top:58px">Tiramisu</div>
      <span class="label" style="top:119px">Quantity</span>
      <div class="field" style="top:138px">250<div class="unit">Milliliters<svg width="11" height="7" viewBox="0 0 11 7"><path d="M1 1l4.5 4.5L10 1" fill="none" stroke="#333" stroke-width="1.3"/></svg></div></div>
    </div>
    <div class="ing-card" style="top:358px;height:200px">
      <div class="head"><svg width="18" height="12" viewBox="0 0 18 12"><path d="M0 0h18l-3 9H3z" fill="#2aa383"/><rect x="4" y="10" width="10" height="2" fill="#2aa383"/></svg>Ingredients 2</div>
      <span class="label" style="top:34px">Ingredient Name</span>
      <div class="field" style="top:58px">Sugar</div>
      <span class="label" style="top:119px">Quantity</span>
      <div class="field" style="top:138px">0<div class="unit">As Needed<svg width="11" height="7" viewBox="0 0 11 7"><path d="M1 1l4.5 4.5L10 1" fill="none" stroke="#333" stroke-width="1.3"/></svg></div></div>
    </div>
    <div class="add" style="top:574px"><b>+</b>Add Another Ingredient</div>
    <div class="next">Next <svg width="16" height="12" viewBox="0 0 16 12"><path d="M1 6h13M9 1l5 5-5 5" fill="none" stroke="#fff" stroke-width="1.7" stroke-linecap="round" stroke-linejoin="round"/></svg></div>
  </section>

  <svg class="flow" width="1568" height="2352" viewBox="0 0 1568 2352" aria-hidden="true">
    <g fill="none" stroke="var(--red)" stroke-width="1.6">
      <path d="M536 727H598"/>
      <path d="M1329 739H1377V1242H588V1262"/>
      <path d="M614 1753H792"/>
    </g>
    <g fill="var(--red)">
      <circle cx="536" cy="727" r="6"/><path d="M596 721l11 6-11 6z"/>
      <circle cx="1329" cy="739" r="6"/><path d="M582 1260l6 11 6-11z"/>
      <circle cx="614" cy="1753" r="6"/><path d="M790 1747l11 6-11 6z"/>
    </g>
  </svg>
</div>
</body>
</html>
```